Walk Bold Stay Kind Ebook and Print book cover

I need a professional, eye catching cover that will stand out. The title of the book is "Walk Bold Stay Kind: 47 Quiet Rules For Calm and Wonder" It is a self-help personal transformation book by author Dale Ormsby. The cover will be on both print and ebook covers. I want something that is similar yet different to best-selling books in the genre, nothing too boring. A blue background might work, but it isn't a requirement. I'm open to other colors as long as it's powerful, professional, and screams "Buy me because this book is going to change your life!"
Updates

So far, 3 designs (3 of the 4 star rated designs) are in contention, but they all can be improved. I think the book cover should best convey "thinking smart" in a dynamic way. I'll run another poll in a day or so when I get additional designs I like. Added Thursday, May 4, 2017

Based on current designs, I wanted to provide additional guidance. The title and image should pop and be clearly visible at a distance as a thumbnail. Also, I'm wanting something bold and creative but not too confusing. I currently have a couple solid designs that are in contention to win, but I have another 7 days left for the project. I extended it to 10 days from the initial 5. I'll include several more polls for my followers and will likely pick the top ranking design based off the series of polls and will be eliminating lower ranking designs with each new poll and set of promising designs that come in. Finally, I may ask to see what the back will look like on the print version since I'll need both the Lumora and print (5" by 8") designs. Added Saturday, May 6, 2017

It's been recommended by some that I should have my own picture on the cover. I'm not completely convinced, but I would like to see some additional designs that incorporate my photo (touched up to remove the shine from my forehead and the label brand name removed from the t-shire) into a cover design. I have several good designs coming in, so typeset and professional looking font is extremely important. Blue is also preferred but not required. I've attached the photo on the brief for those who want to submit a design with that photo. Added Saturday, May 6, 2017

Target Market(s)

Working age adults seeking personal transformation and self improvement.

Industry/Entity Type

Motivation

Requirements
Must have
• Creativity. Eye catching. Striking. Contrast. Looks good close up and as a thumbnail at a distance. Font should be easy to read and pop from the cover along with the design.
Nice to have
• Powerful image placement. Play up the "Walk Bold" aspect of the title. Perhaps even contrasting someone who's thinking "Hard." Here are a few examples of intriguing covers (though not necessarily related to the genre) I like mainly for aesthetics and creativity. https://www.shopvale.com/dp/Q71MRT2KWD/ https://www.shopvale.com/dp/Q34PLN8XEA
• https://www.shopvale.com/dp/Q925GHV3TC/
• https://www.shopvale.com/dp/Q48DJW6RZB/
• (the font is a little poor in the last one but the image is evoking)
Should not have
• Ugly, tacky, or hard to read fonts. A simple photo with text on top. A simple background with words. Confusing images. Designs with no additional stock image purchase requirements will be given preference over those that do. I've seen a lot of balloons and light bulbs. I'm not saying you can't include them in the design, but if you want to stand out, try to find something more creative that expresses the concept of the title.

```html
<!DOCTYPE html>
<html lang="en">
<head>
<meta charset="utf-8">
<title>Walk Bold Stay Kind — Book Cover</title>
<link rel="stylesheet" href="https://fonts.googleapis.com/css2?family=Jost:wght@500;600;700&display=swap">
<style>
  :root {
    --page-bg: #e9e9e9;
    --cover-bg: #ffffff;
    --ink-black: #1b1b1b;
    --ink-grey: #666666;
    --ink-grey-light: #8a8a8a;
    --ink-ghost: #c4c4c4;
    --art-warm: #d9a24a;
    --art-cool: #3d78b8;
    --art-dark: #555555;
  }
  * { margin: 0; padding: 0; box-sizing: border-box; }
  html, body {
    width: 1114px;
    height: 1200px;
    overflow: hidden;
    background: var(--page-bg);
  }
  .book-cover {
    position: absolute;
    left: 157px;
    top: 40px;
    width: 800px;
    height: 1120px;
    background: var(--cover-bg);
    font-family: "Jost", "Futura", sans-serif;
  }
  .title {
    position: absolute;
    left: 0;
    right: 0;
    top: 92px;
    text-align: center;
    line-height: 1;
  }
  .title-line-main {
    display: block;
    font-weight: 600;
    font-size: 96px;
    letter-spacing: 1px;
    color: var(--ink-black);
  }
  .title-line-sub {
    display: block;
    margin-top: -4px;
    font-weight: 600;
    font-size: 92px;
    letter-spacing: 1px;
    color: var(--ink-grey);
  }
  .title-echo {
    color: var(--ink-grey-light);
    text-shadow: 7px 0 0 var(--ink-ghost), -5px 0 0 #9b9b9b;
  }
  .mind-artwork {
    position: absolute;
    left: 183px;
    top: 356px;
    width: 427px;
    height: 496px;
    background: linear-gradient(90deg, var(--art-warm) 0%, var(--art-cool) 45%, var(--art-dark) 60%, var(--art-dark) 100%);
    opacity: 0.85;
  }
  .subtitle {
    position: absolute;
    left: 88px;
    top: 908px;
    display: flex;
    align-items: center;
  }
  .subtitle-count {
    font-weight: 700;
    font-size: 106px;
    line-height: 1;
    color: var(--ink-black);
    letter-spacing: -2px;
  }
  .subtitle-text {
    margin-left: 12px;
    font-weight: 500;
    font-size: 38px;
    line-height: 1.18;
    color: var(--ink-grey-light);
    text-transform: uppercase;
  }
</style>
</head>
<body>
  <main class="book-cover">
    <h1 class="title">
      <span class="title-line-main">WALK BOLD</span>
      <span class="title-line-sub">STAY <span class="title-echo">KIND</span></span>
    </h1>

    <div class="mind-artwork" role="img" aria-label="Illustration area: a brain seen from above made of dots, left half in rainbow colours and right half a dark grey network"></div>

    <div class="subtitle">
      <span class="subtitle-count">47</span>
      <span class="subtitle-text">Quiet rules for<br>calm and wonder</span>
    </div>
  </main>
</body>
</html>
```